Melissa Dorvan Personal Business Card

I like orange. It's would better if my card have an orange background
Address: 5820 Halvers Lane #417
San Jose
California
US
Tel: 4085172049

Industry/Entity Type

Business

```html
<!DOCTYPE html>
<html lang="en">
<head>
<meta charset="utf-8">
<title>Melissa Dorvan – Business Card</title>
<link rel="stylesheet" href="https://fonts.googleapis.com/css2?family=Cinzel:wght@700;800&display=swap">
<style>
  :root {
    --backdrop: #262626;
    --wood-dark: #4e1c07;
    --wood-mid: #8a3a0d;
    --wood-light: #c2620f;
    --plate-glow: #f3bd45;
    --plate-mid: #d08a1c;
    --plate-edge: #8e4f0b;
    --plate-rim: #5a2e08;
    --rivet-light: #e8c070;
    --rivet-dark: #6a4210;
    --silver-light: #ffffff;
    --silver-mid: #b9bcc2;
    --silver-dark: #5d6168;
    --ink-light: #fbf6ea;
  }
  * { box-sizing: border-box; margin: 0; padding: 0; }
  html, body {
    width: 1200px;
    height: 797px;
    overflow: hidden;
    background: var(--backdrop);
  }
  .business-card {
    position: absolute;
    left: 150px;
    top: 141px;
    width: 900px;
    height: 515px;
    border-radius: 4px;
    background:
      linear-gradient(180deg, rgba(255,190,90,0.35) 0%, rgba(0,0,0,0) 12%, rgba(0,0,0,0) 88%, rgba(0,0,0,0.35) 100%),
      linear-gradient(90deg, var(--wood-dark) 0%, var(--wood-mid) 18%, var(--wood-light) 50%, var(--wood-mid) 82%, var(--wood-dark) 100%);
    box-shadow: 0 14px 40px rgba(0,0,0,0.6);
    font-family: "Cinzel", "Times New Roman", serif;
  }
  .card-plate {
    position: absolute;
    inset: 36px;
    border: 2px solid var(--plate-rim);
    background: radial-gradient(ellipse at 55% 40%, var(--plate-glow) 0%, var(--plate-mid) 50%, var(--plate-edge) 100%);
    box-shadow: inset 0 0 24px rgba(60,25,0,0.55), 0 0 6px rgba(0,0,0,0.5);
  }
  .rivet {
    position: absolute;
    width: 16px;
    height: 16px;
    border-radius: 50%;
    background: radial-gradient(circle at 35% 35%, var(--rivet-light), var(--rivet-dark));
    box-shadow: 0 1px 2px rgba(0,0,0,0.6);
  }
  .rivet.top-left { left: 52px; top: 52px; }
  .rivet.top-right { right: 52px; top: 52px; }
  .rivet.bottom-left { left: 52px; bottom: 52px; }
  .rivet.bottom-right { right: 52px; bottom: 52px; }
  .holder-name {
    position: absolute;
    left: 110px;
    top: 120px;
    font-size: 74px;
    font-weight: 800;
    font-variant: small-caps;
    letter-spacing: 2px;
    line-height: 1;
    background: linear-gradient(180deg, var(--silver-light) 0%, var(--silver-mid) 48%, var(--silver-dark) 52%, var(--silver-light) 100%);
    -webkit-background-clip: text;
    background-clip: text;
    color: transparent;
    filter: drop-shadow(3px 4px 3px rgba(40,15,0,0.75));
  }
  .contact {
    position: absolute;
    color: var(--ink-light);
    font-size: 20px;
    font-weight: 700;
    font-variant: small-caps;
    letter-spacing: 0.5px;
    text-shadow: 1px 1px 2px rgba(40,15,0,0.7);
    line-height: 1.2;
  }
  .contact-phone { left: 96px; top: 410px; }
  .contact-address { left: 440px; top: 352px; }
  .contact-address .locality { display: block; padding-left: 138px; }
</style>
</head>
<body>
  <div class="business-card">
    <div class="card-plate" role="img" aria-label="Golden metal plate with a raised diamond dot pattern"></div>
    <span class="rivet top-left"></span>
    <span class="rivet top-right"></span>
    <span class="rivet bottom-left"></span>
    <span class="rivet bottom-right"></span>
    <h1 class="holder-name">Melissa Dorvan</h1>
    <p class="contact contact-address">
      Address: 5820 Halvers Lane #417
      <span class="locality">San Jose California US</span>
    </p>
    <p class="contact contact-phone">Tel: 4085172049</p>
  </div>
</body>
</html>
```